Fresh new and cool frozen burger box! Come be a part of an amazing project!

Crust Fries and Melts restaurant is expanding into the frozen foods market!
please check out our website to understand the vibe of the company
https://grillvexa.ca
this is a line of premium Halal meat, we want to stress our top-notch quality.
we like the orange colours so see what you can do with them. (maybe white and orange combo)
you have lots of creative freedom here, feel free to use the burger photo I am attaching or any image off the website.
logo should be nice and visible.
we want this packaging to really stand out and be special.
Come be a part of an amazing project!
Target Market(s)
Muslim Flails, looking of a quality meat burger. mostly already familiar with our brand
Industry/Entity Type
Frozen food
Look and feel

```html
<!DOCTYPE html>
<html lang="en">
<head>
<meta charset="utf-8">
<title>Grillvexa burger box dieline</title>
<link rel="stylesheet" href="https://fonts.googleapis.com/css2?family=Oswald:wght@700&family=Open+Sans:wght@700;800&family=Kaushan+Script&display=swap">
<style>
  :root{
    --orange:#f39220;
    --brand-orange:#f0901e;
    --ink:#141414;
    --paper:#ffffff;
    --paper-soft:#f2f2f2;
    --night:#0d0907;
    --flame-red:#e2262b;
    --bun:#e9a24e;
    --bun-deep:#b8551f;
  }
  *{box-sizing:border-box;margin:0;padding:0}
  html,body{width:762px;height:1200px;overflow:hidden;background:var(--orange)}
  body{position:relative;font-family:"Open Sans",sans-serif}

  .dieline{position:absolute;left:0;top:212px;width:762px;height:776px}
  .panel{position:absolute;overflow:hidden}

  .top-flap{left:157px;top:48px;width:454px;height:178px;background:linear-gradient(90deg,var(--paper-soft),var(--paper) 55%)}
  .top-flap .flip{position:absolute;inset:0;transform:rotate(180deg)}

  .side-left{left:17px;top:226px;width:137px;height:349px;background:var(--paper)}
  .front{left:154px;top:226px;width:457px;height:349px;background:linear-gradient(90deg,var(--paper-soft),var(--paper) 40%)}
  .side-right{left:611px;top:226px;width:130px;height:349px;background:var(--ink)}
  .bottom{left:154px;top:575px;width:457px;height:152px;background:linear-gradient(90deg,var(--paper-soft),var(--paper) 40%)}

  .night-side{position:absolute;top:0;bottom:0;right:0;
    background:radial-gradient(circle at 70% 12%,rgba(200,110,40,.55),rgba(13,9,7,0) 45%),
               radial-gradient(circle at 35% 8%,rgba(180,100,40,.35),rgba(13,9,7,0) 30%),var(--night)}
  .front .night-side{left:168px;clip-path:polygon(2% 0,0 6%,3% 14%,1% 22%,3% 31%,0 40%,3% 50%,1% 60%,3% 70%,0 80%,3% 90%,1% 100%,100% 100%,100% 0)}
  .bottom .night-side{left:164px;background:var(--night);clip-path:polygon(4% 0,1% 15%,4% 30%,2% 50%,4% 65%,1% 82%,3% 100%,100% 100%,100% 0)}

  .lockup{position:absolute;display:flex;align-items:center;gap:8px}
  .brand-mark{width:46px;height:46px;border-radius:50%;border:3px solid var(--flame-red);flex:none}
  .brand-name{font-family:"Oswald",sans-serif;font-weight:700;color:var(--brand-orange);font-size:54px;line-height:1;letter-spacing:-.5px}
  .tagline{position:absolute;display:flex;align-items:center;font-weight:800;font-size:20px;line-height:1;white-space:nowrap;color:var(--ink)}
  .tagline .dot{color:var(--flame-red);font-size:.7em;margin:0 5px}
  .tagline .lead{display:inline-block;width:72px;text-align:right}
  .tagline .on-night{color:var(--paper)}

  .front .lockup{left:95px;top:40px}
  .front .tagline{left:88px;top:102px}
  .bottom .lockup{left:93px;top:40px}
  .bottom .tagline{left:88px;top:104px}

  .offer{position:absolute;left:44px;top:180px;font-weight:800;font-size:22px;color:var(--brand-orange);line-height:1}
  .offer-rule{position:absolute;left:48px;top:206px;width:92px;height:2px;background:var(--brand-orange)}
  .order-badge{position:absolute;left:51px;top:229px;width:82px;height:82px;border-radius:50%;background:var(--brand-orange);display:flex;align-items:center;justify-content:center}
  .order-badge::before{content:"";position:absolute;inset:4px;border:1.5px solid var(--paper);border-radius:50%}
  .order-text{font-family:"Kaushan Script",cursive;color:var(--ink);font-size:18px;line-height:.95;text-align:center;transform:rotate(-10deg)}
  .call{position:absolute;left:22px;top:317px;display:flex;align-items:center;gap:8px}
  .call-icon{width:26px;height:26px;border-radius:50%;background:var(--brand-orange);display:flex;align-items:center;justify-content:center}
  .call-number{font-weight:800;font-size:14px;color:var(--brand-orange)}

  .burger-photo{position:absolute;left:205px;top:142px;width:233px;height:190px;border-radius:48% 48% 40% 40%;
    background:radial-gradient(ellipse at 50% 30%,#f2b868,var(--bun) 35%,#c0392b 55%,#6b3a1a 65%,#5e9a2c 78%,var(--bun-deep) 90%)}

  .burger-disc{position:absolute;border-radius:50%;border:3px solid var(--ink);background:var(--paper);padding:4px}
  .burger-disc .fill{width:100%;height:100%;border-radius:50%;
    background:radial-gradient(circle,var(--bun) 0,#c0392b 35%,#6b3a1a 50%,#4e8a26 62%,var(--night) 80%)}
  .side-left .burger-disc{left:17px;top:27px;width:104px;height:104px}
  .top-flap .burger-disc{left:37px;top:21px;width:134px;height:136px}

  .side-left .vertical{position:absolute;left:104px;top:145px;width:180px;transform-origin:0 0;transform:rotate(90deg)}
  .vertical .lockup{position:relative;gap:6px}
  .vertical .brand-mark{width:30px;height:30px;border-width:2px}
  .vertical .brand-name{font-size:34px;color:var(--ink)}
  .vertical .tagline{position:relative;font-size:12px;margin-top:4px}

  .top-flap .lockup{left:190px;top:40px}
  .top-flap .brand-mark{width:40px;height:40px;border-width:2.5px}
  .top-flap .brand-name{font-size:44px;color:var(--ink)}
  .top-flap .tagline{left:200px;top:100px;font-size:16px}

  .delivery{position:absolute;transform-origin:0 0;transform:rotate(-90deg);width:240px;font-weight:800;line-height:1}
  .delivery .headline{color:var(--paper);font-size:25px;letter-spacing:.5px}
  .delivery .number{color:var(--brand-orange);font-size:25px;margin-top:11px;padding-left:14px}
  .side-right .delivery{left:34px;top:296px}
</style>
</head>
<body>
<main class="dieline">

  <section class="panel top-flap">
    <div class="flip">
      <div class="burger-disc"><div class="fill" role="img" aria-label="Photo of a bacon cheeseburger in a black circle"></div></div>
      <div class="lockup"><span class="brand-mark"></span><span class="brand-name">GRILLVEXA</span></div>
      <p class="tagline">Crust<span class="dot">•</span>Fries<span class="dot">•</span>Melts</p>
    </div>
  </section>

  <section class="panel side-left">
    <div class="burger-disc"><div class="fill" role="img" aria-label="Photo of a bacon cheeseburger seen from the side in a black circle"></div></div>
    <div class="vertical">
      <div class="lockup"><span class="brand-mark"></span><span class="brand-name">GRILLVEXA</span></div>
      <p class="tagline">Crust<span class="dot">•</span>Fries<span class="dot">•</span>Melts</p>
    </div>
  </section>

  <section class="panel front">
    <div class="night-side"></div>
    <div class="burger-photo" role="img" aria-label="Photo of a bacon cheeseburger with tomato, cheese and lettuce"></div>
    <div class="lockup"><span class="brand-mark"></span><span class="brand-name">GRILLVEXA</span></div>
    <p class="tagline"><span class="lead">Crust</span><span class="dot">•</span><span class="on-night">Fries</span><span class="dot">•</span><span class="on-night">Melts</span></p>
    <p class="offer">10% OFF</p>
    <div class="offer-rule"></div>
    <div class="order-badge"><span class="order-text">Order<br>Now!</span></div>
    <div class="call">
      <span class="call-icon">
        <svg width="14" height="14" viewBox="0 0 24 24" aria-hidden="true"><path fill="#fff" d="M6.6 10.8a15.1 15.1 0 0 0 6.6 6.6l2.2-2.2a1 1 0 0 1 1-.25 11.4 11.4 0 0 0 3.6.57 1 1 0 0 1 1 1V20a1 1 0 0 1-1 1A17 17 0 0 1 3 4a1 1 0 0 1 1-1h3.5a1 1 0 0 1 1 1c0 1.25.2 2.45.57 3.6a1 1 0 0 1-.25 1z"/></svg>
      </span>
      <span class="call-number">+1 555 0142</span>
    </div>
  </section>

  <section class="panel side-right">
    <div class="delivery">
      <p class="headline">FREE DELIVERY</p>
      <p class="number">+1 555-0142</p>
    </div>
  </section>

  <section class="panel bottom">
    <div class="night-side"></div>
    <div class="lockup"><span class="brand-mark"></span><span class="brand-name">GRILLVEXA</span></div>
    <p class="tagline"><span class="lead">Crust</span><span class="dot">•</span><span class="on-night">Fries</span><span class="dot">•</span><span class="on-night">Melts</span></p>
  </section>

</main>
</body>
</html>
```